Pellory T's Menu boxes

HI

This project if for the design of some illuminated menu boxes for inside a shop.

We sell Ice Cream, Milk shakes, Smoothies and some cakes.

The shop is mainly pink in colour, i have had some posters done for the windows and would like the menus to maintain the feel of the posters. i have 8 menu boards but will probably onlu use 4.

i will attach a few of the posters so you can see the feel im looking for and the menu should have:
a section for ice creams
a section for milk shakes
a section for smoothies
a section for coffees and teas
and a section for juices
and a section for desserts.

Regards
Updates

Hi

I have now attached the logos source file

Many thanks

Reason: Hi for some reason only one designer has responded therefore i am extending the deadline thanks

Hi All

I have now increased the budget on the project

Many Thanks

```html
<!DOCTYPE html>
<html lang="en">
<head>
<meta charset="utf-8">
<title>Pellory T's Menu Boards</title>
<link href="https://fonts.googleapis.com/css2?family=Fredoka:wght@500;600;700&display=swap" rel="stylesheet">
<style>
:root{
  --bg-center:#ffffff;
  --bg-edge:#d2d3d5;
  --board-fill:#ffffff;
  --plum:#8b2a8f;
  --teal:#1a9aa8;
  --magenta:#e4007c;
  --band:#ffe600;
  --band-shadow:#8b2a8f;
  --note:#7a2a86;
}
*{margin:0;padding:0;box-sizing:border-box}
html,body{width:1200px;height:848px;overflow:hidden}
body{
  position:relative;
  background:radial-gradient(ellipse at 50% 50%,var(--bg-center) 0%,var(--bg-edge) 75%);
  font-family:"Fredoka",sans-serif;
}
.board{position:absolute;top:196px;width:382px;height:274px}
.board-frame{position:absolute;inset:0;width:100%;height:100%}
.pos{position:absolute;white-space:nowrap;line-height:1}
.brand{font-weight:700;font-size:19px;color:var(--magenta)}
.product-photo{position:absolute;border-radius:10px}
.section-title{
  font-weight:700;font-size:19px;color:var(--magenta);
  text-shadow:-1px -1px 0 #fff,1px -1px 0 #fff,-1px 1px 0 #fff,1px 1px 0 #fff,2px 2px 0 var(--plum);
}
.size-label,.price{
  font-weight:700;color:var(--magenta);
  text-shadow:-1px -1px 0 #fff,1px -1px 0 #fff,-1px 1px 0 #fff,1px 1px 0 #fff,1.5px 1.5px 0 var(--plum);
}
.size-label{font-size:14px}
.price{font-size:12px}
.group-label{font-weight:700;font-size:13px;color:var(--magenta);text-shadow:1px 1px 0 var(--plum)}
.flavour-band{
  position:absolute;background:var(--band);
  border-radius:0 6px 6px 0;
  box-shadow:4px 4px 0 var(--band-shadow);
}
.flavour{font-weight:600;font-size:11.5px;color:var(--magenta)}
.extra{font-weight:600;font-size:11.5px;color:var(--note)}
.booster{font-weight:500;font-size:7px;color:var(--magenta)}
</style>
</head>
<body>

<!-- Smoothies board -->
<section class="board" style="left:8px">
  <svg class="board-frame" viewBox="0 0 382 274" aria-hidden="true">
    <path d="M2,270 V82 C2,30 85,3 191,3 C297,3 380,30 380,82 V270 Z" fill="var(--board-fill)" stroke="var(--plum)" stroke-width="3.5"/>
  </svg>
  <div class="pos brand" style="left:146px;top:30px">Pellory T's</div>
  <div class="product-photo" role="img" aria-label="Glasses of smoothie with straws, kiwi and banana" style="left:240px;top:36px;width:96px;height:110px;background:linear-gradient(180deg,#f4e3c8 0%,#d8403e 55%,#9cbf3c 100%)"></div>
  <div class="pos section-title" style="left:5px;top:110px">Smoothies</div>
  <div class="pos size-label" style="left:150px;top:92px">S</div>
  <div class="pos size-label" style="left:183px;top:92px">M</div>
  <div class="pos size-label" style="left:218px;top:92px">L</div>
  <div class="pos price" style="left:141px;top:116px">3.95</div>
  <div class="pos price" style="left:176px;top:116px">4.55</div>
  <div class="pos price" style="left:210px;top:116px">4.95</div>
  <div class="flavour-band" style="left:4px;top:150px;width:343px;height:64px"></div>
  <div class="pos flavour" style="left:8px;top:154px">Strawberry Kiwi</div>
  <div class="pos flavour" style="left:8px;top:169px">Lime Infusion</div>
  <div class="pos flavour" style="left:8px;top:184px">Verry Berry</div>
  <div class="pos flavour" style="left:8px;top:199px">Lychee Passion Fruit</div>
  <div class="pos flavour" style="left:133px;top:154px">Banana Chocolate</div>
  <div class="pos flavour" style="left:133px;top:169px">Orange Pineapple</div>
  <div class="pos flavour" style="left:133px;top:184px">Pellory Mix</div>
  <div class="pos flavour" style="left:133px;top:199px">Apple Pear</div>
  <div class="pos flavour" style="left:258px;top:154px">Pina Colada</div>
  <div class="pos flavour" style="left:258px;top:169px">Peach Mango</div>
  <div class="pos flavour" style="left:258px;top:184px">Coconut Dream</div>
  <div class="pos flavour" style="left:258px;top:199px">Guava Peach</div>
  <div class="pos extra" style="left:7px;top:230px">Add Health Boosters</div>
  <div class="pos extra" style="left:138px;top:230px">1.50</div>
  <div class="pos booster" style="left:42px;top:249px">Wheat Grass</div>
  <div class="pos booster" style="left:98px;top:249px">Gluten Free Protein</div>
  <div class="pos booster" style="left:178px;top:249px">Brain Complex</div>
  <div class="pos booster" style="left:246px;top:249px">Omega 3</div>
</section>

<!-- Milkshakes board -->
<section class="board" style="left:402px">
  <svg class="board-frame" viewBox="0 0 382 274" aria-hidden="true">
    <path d="M2,270 V75 C2,55 15,45 35,45 C40,25 65,18 82,30 C92,8 128,4 142,22 C152,4 188,4 198,20 C208,4 244,4 254,22 C266,8 296,10 304,30 C322,22 348,30 352,50 C370,52 380,65 380,85 V270 Z" fill="var(--board-fill)" stroke="var(--teal)" stroke-width="3.5"/>
  </svg>
  <div class="pos brand" style="left:142px;top:30px">Pellory T's</div>
  <div class="product-photo" role="img" aria-label="Chocolate milkshake glass with cream and a cherry" style="left:258px;top:26px;width:66px;height:118px;background:linear-gradient(180deg,#f3efe9 0%,#7a4a32 60%,#dcdcdc 100%)"></div>
  <div class="pos section-title" style="left:5px;top:110px">Milkshakes</div>
  <div class="pos size-label" style="left:150px;top:92px">S</div>
  <div class="pos size-label" style="left:182px;top:92px">M</div>
  <div class="pos size-label" style="left:217px;top:92px">L</div>
  <div class="pos price" style="left:141px;top:116px">2.95</div>
  <div class="pos price" style="left:175px;top:116px">3.55</div>
  <div class="pos price" style="left:209px;top:116px">3.95</div>
  <div class="flavour-band" style="left:3px;top:150px;width:343px;height:64px"></div>
  <div class="pos flavour" style="left:7px;top:154px">Chocolate</div>
  <div class="pos flavour" style="left:7px;top:169px">Rootbeer</div>
  <div class="pos flavour" style="left:7px;top:184px">Verry Berry</div>
  <div class="pos flavour" style="left:7px;top:199px">Blueberry</div>
  <div class="pos flavour" style="left:132px;top:154px">Vanilla</div>
  <div class="pos flavour" style="left:132px;top:169px">Orange</div>
  <div class="pos flavour" style="left:132px;top:184px">Pellory Mix</div>
  <div class="pos flavour" style="left:132px;top:199px">Marshmallow</div>
  <div class="pos flavour" style="left:258px;top:154px">Strawberry</div>
  <div class="pos flavour" style="left:258px;top:169px">Peach</div>
  <div class="pos flavour" style="left:258px;top:184px">Coconut Dream</div>
  <div class="pos flavour" style="left:258px;top:199px">Rockie Road</div>
</section>

<!-- Ice cream board -->
<section class="board" style="left:800px">
  <svg class="board-frame" viewBox="0 0 382 274" aria-hidden="true">
    <path d="M2,270 V82 C2,30 85,3 191,3 C297,3 380,30 380,82 V270 Z" fill="var(--board-fill)" stroke="var(--plum)" stroke-width="3.5"/>
  </svg>
  <div class="pos brand" style="left:142px;top:30px">Pellory T's</div>
  <div class="product-photo" role="img" aria-label="Three ice cream cones in berry, strawberry and chocolate" style="left:26px;top:32px;width:110px;height:92px;background:linear-gradient(180deg,#a77bc4 0%,#e7829e 45%,#d9a35a 100%)"></div>
  <div class="pos group-label" style="left:152px;top:68px">CONES</div>
  <div class="pos group-label" style="left:287px;top:68px">CUP</div>
  <div class="pos section-title" style="left:4px;top:110px">Ice Cream</div>
  <div class="pos size-label" style="left:136px;top:92px">S</div>
  <div class="pos size-label" style="left:169px;top:92px">M</div>
  <div class="pos size-label" style="left:205px;top:92px">L</div>
  <div class="pos size-label" style="left:262px;top:92px">S</div>
  <div class="pos size-label" style="left:294px;top:92px">M</div>
  <div class="pos size-label" style="left:330px;top:92px">L</div>
  <div class="pos price" style="left:128px;top:116px">1.95</div>
  <div class="pos price" style="left:162px;top:116px">2.55</div>
  <div class="pos price" style="left:195px;top:116px">2.95</div>
  <div class="pos price" style="left:253px;top:116px">2.25</div>
  <div class="pos price" style="left:288px;top:116px">2.85</div>
  <div class="pos price" style="left:322px;top:116px">3.35</div>
  <div class="flavour-band" style="left:2px;top:150px;width:343px;height:64px"></div>
  <div class="pos flavour" style="left:5px;top:154px">Rum Raisin</div>
  <div class="pos flavour" style="left:5px;top:169px">Tiger</div>
  <div class="pos flavour" style="left:5px;top:184px">Strawberry</div>
  <div class="pos flavour" style="left:5px;top:199px">Lychee Passion Fruit</div>
  <div class="pos flavour" style="left:130px;top:154px">Chocolate Mint</div>
  <div class="pos flavour" style="left:130px;top:169px">Peanut Butter Ripple</div>
  <div class="pos flavour" style="left:130px;top:184px">Cherry Cheesecake</div>
  <div class="pos flavour" style="left:130px;top:199px">Apple Pear</div>
  <div class="pos flavour" style="left:256px;top:154px">Bubblegum</div>
  <div class="pos flavour" style="left:256px;top:169px">Vanilla</div>
  <div class="pos flavour" style="left:256px;top:184px">Mocha Java</div>
  <div class="pos flavour" style="left:256px;top:199px">Guava Peach</div>
  <div class="pos extra" style="left:6px;top:230px">Add Wafer Cone</div>
  <div class="pos extra" style="left:119px;top:230px">.55</div>
  <div class="pos extra" style="left:191px;top:230px">Add Topping</div>
  <div class="pos extra" style="left:282px;top:230px">.35each</div>
</section>

</body>
</html>
```